dkfarrowplace website

I need a new homepage design for my current website at www.DKFarrowPlace.example. I want someone to look at my current website and develop a more appealing homepage... right now the colors don't blend very well and it needs a facelift

Reason: This has been extended to September 10th

```html
<!DOCTYPE html>
<html lang="en">
<head>
<meta charset="utf-8">
<title>DK Farrow – Home</title>
<link rel="stylesheet" href="https://fonts.googleapis.com/css2?family=Gelasio:wght@400;500&family=Figtree:wght@300;400;600;700&family=Roboto+Condensed:ital,wght@0,400;0,700;1,400&display=swap">
<style>
:root{
  --teal:#177f98;
  --teal-bright:#1a9bbf;
  --lime:#8cc63f;
  --lime-bright:#a6d92a;
  --dark-green:#3f7f2a;
  --ink:#333;
  --white:#fff;
}
*{margin:0;padding:0;box-sizing:border-box}
html,body{width:1050px;height:1200px;overflow:hidden;background:var(--white);font-family:"Figtree",sans-serif;color:var(--ink)}
.page{position:relative;width:1050px;height:1200px}
.abs{position:absolute}

.brand{left:175px;top:6px;font-family:"Gelasio",serif;font-size:44px;color:var(--teal);letter-spacing:-1px;line-height:56px;white-space:nowrap}
.follow{left:624px;top:16px;font-size:21px;font-weight:300;color:var(--teal);letter-spacing:1px}
.social{top:7px;width:40px;height:40px;border-radius:50%;background:var(--teal-bright);border:3px solid #dfe3e6}
.social.one{left:795px}.social.two{left:844px;background:#3b5b9a}

.nav{left:0;top:66px;width:1050px;height:48px;background:linear-gradient(#a8dc1e,#7ec32a)}
.nav ul{list-style:none}
.nav li{position:absolute;top:16px;font-size:14.5px;color:var(--white);letter-spacing:.2px;white-space:nowrap}
.nav-active{left:181px;top:114px;width:60px;height:6px;background:var(--teal)}

.hero{left:0;top:120px;width:1050px;height:321px;background:linear-gradient(#fff 0%,#fff 70%,#ececec 100%)}
.hero-title{left:177px;top:162px;font-family:"Gelasio",serif;font-weight:400;font-size:47px;line-height:54px;color:var(--teal)}
.hero-title .g{color:var(--lime)}
.btn{border:2px solid var(--teal);color:var(--teal);font-size:17px;display:flex;align-items:center;justify-content:center;letter-spacing:.5px}
.hero-btn{left:179px;top:357px;width:141px;height:41px}
.hero-photo{left:500px;top:130px;width:425px;height:311px;background:radial-gradient(ellipse at 50% 45%,#d9b39a 0%,#c9a189 30%,#f3f0ee 65%,rgba(255,255,255,0) 80%)}

.report-title{left:175px;top:490px;font-family:"Gelasio",serif;font-weight:400;font-size:46px;color:var(--teal-bright);white-space:nowrap}
.report-sub{left:174px;top:549px;font-size:20px;color:var(--lime)}
.report-text{left:177px;top:583px;width:360px;font-size:14.5px;line-height:22px;color:var(--ink)}
.label{left:579px;font-size:20px;font-weight:300;color:var(--lime)}
.field{left:577px;width:316px;height:32px;border:3px solid var(--teal-bright)}
.subscribe{left:773px;top:635px;width:121px;height:38px;border:3px solid var(--lime);color:var(--teal-bright);font-size:15px;font-weight:300}

.promo{left:150px;top:717px;width:750px;height:228px;background:linear-gradient(#a6d92a,#7dc12f);padding:13px}
.promo-inner{width:100%;height:100%;background:linear-gradient(90deg,#e9f8dd,#f3fbe9 60%,#c8efe0)}
.promo-title{left:228px;top:756px;font-weight:700;color:var(--dark-green);line-height:1;white-space:nowrap}
.promo-title .l1{font-size:40px;color:var(--teal)}
.promo-title .l2{font-size:50px;letter-spacing:-1px}
.promo-title .l3{font-size:28px;font-weight:400;letter-spacing:9px;color:var(--teal);margin-left:62px}
.promo-tag{left:228px;top:884px;font-family:"Roboto Condensed",sans-serif;font-size:18px;font-weight:700;color:var(--dark-green);white-space:nowrap}
.promo-avail{left:577px;top:885px;font-family:"Roboto Condensed",sans-serif;font-size:16px;font-style:italic;color:var(--teal);white-space:nowrap}
.promo-by{left:305px;top:909px;font-size:13px;color:var(--lime);white-space:nowrap}
.promo-badge{left:581px;top:767px;width:99px;height:99px;border-radius:50%;background:var(--teal-bright);color:var(--white);font-family:"Roboto Condensed",sans-serif;font-size:13.5px;font-weight:700;text-align:center;display:flex;align-items:center;justify-content:center;line-height:17px}
.promo-book{left:708px;top:726px;width:120px;height:176px;background:linear-gradient(160deg,#f5f8f0,#a9d47e 55%,#3e8a3a)}

.seen-title{left:175px;top:957px;font-family:"Gelasio",serif;font-weight:400;font-size:44px;color:var(--teal)}
.seen-strip{left:0;top:1028px;width:1050px;height:66px;border-top:2px solid var(--teal-bright);border-bottom:2px solid var(--teal-bright)}
.partner{top:1046px;height:30px;border-radius:3px}
.divider{top:1042px;height:38px;border-left:2px dotted var(--lime)}

.footer-links,.footer-copy{left:0;width:1050px;text-align:center;font-size:14px;color:var(--teal)}
.footer-links{top:1142px}
.footer-copy{top:1162px}
</style>
</head>
<body>
<div class="page">
  <header>
    <div class="abs brand">DK FARROW</div>
    <div class="abs follow">FOLLOW US ON</div>
    <span class="abs social one" role="img" aria-label="Social profile one"></span>
    <span class="abs social two" role="img" aria-label="Social profile two"></span>
    <nav class="abs nav">
      <ul>
        <li style="left:197px">HOME</li>
        <li style="left:277px">ABOUT</li>
        <li style="left:363px">PRODUCTS</li>
        <li style="left:477px">BLOG</li>
        <li style="left:552px">SUCCESS ROOM</li>
        <li style="left:702px">FORUM</li>
        <li style="left:792px">MEDIA ROOM</li>
      </ul>
    </nav>
    <div class="abs nav-active"></div>
  </header>

  <section>
    <div class="abs hero"></div>
    <div class="abs hero-photo" role="img" aria-label="Photo of a smiling fit woman holding a measuring tape around her waist"></div>
    <h1 class="abs hero-title"><span class="g">DISCOVER</span> Secrets to<br><span class="g">a</span> Slimmer<span class="g">,</span> Sexier <span class="g">&amp;</span><br>Healthier <span class="g">You</span></h1>
    <div class="abs btn hero-btn">READ MORE</div>
  </section>

  <section>
    <h2 class="abs report-title">Get Free Report</h2>
    <p class="abs report-sub">“5 Reasons You Can’t Lose Weight!”</p>
    <p class="abs report-text">Just enter your name and email below to get instant access to this 30 page report absolutely FREE!</p>
    <div class="abs label" style="top:487px">NAME</div>
    <div class="abs field" style="top:520px"></div>
    <div class="abs label" style="top:561px">E-MAIL</div>
    <div class="abs field" style="top:594px"></div>
    <div class="abs btn subscribe">SUBSCRIBE</div>
  </section>

  <section>
    <div class="abs promo"><div class="promo-inner"></div></div>
    <div class="abs promo-title">
      <div class="l1">10-DAY FRESH</div>
      <div class="l2">BLEND</div>
      <div class="l3">RESET</div>
    </div>
    <div class="abs promo-tag">LOSE WEIGHT. GET HEALTHY. FEEL ENERGIZED.</div>
    <div class="abs promo-avail">Available Now</div>
    <div class="abs promo-badge">LOSE UP TO<br>15 POUNDS<br>IN 10 DAYS!</div>
    <div class="abs promo-book" role="img" aria-label="Book cover with green drink and fresh produce"></div>
    <div class="abs promo-by">By DK Farrow, #1 Bestselling Author, Nutritionist and Weight-Loss Expert</div>
  </section>

  <section>
    <h2 class="abs seen-title">As Seen On</h2>
    <div class="abs seen-strip"></div>
    <svg class="abs" style="left:149px;top:1051px" width="20" height="20" viewBox="0 0 20 20" aria-label="Previous"><circle cx="10" cy="10" r="10" fill="#1a9bbf"/><path d="M12 5l-5 5 5 5" stroke="#fff" stroke-width="2" fill="none"/></svg>
    <svg class="abs" style="left:880px;top:1051px" width="20" height="20" viewBox="0 0 20 20" aria-label="Next"><circle cx="10" cy="10" r="10" fill="#1a9bbf"/><path d="M8 5l5 5-5 5" stroke="#fff" stroke-width="2" fill="none"/></svg>
    <div class="abs partner" style="left:195px;width:84px;background:#222"></div>
    <div class="abs divider" style="left:302px"></div>
    <div class="abs partner" style="left:324px;width:68px;background:#3a8a1e"></div>
    <div class="abs divider" style="left:411px"></div>
    <div class="abs partner" style="left:433px;width:140px;height:22px;top:1050px;background:#9c1b3c"></div>
    <div class="abs divider" style="left:595px"></div>
    <div class="abs partner" style="left:620px;width:68px;background:#0d3a8c"></div>
    <div class="abs divider" style="left:712px"></div>
    <div class="abs partner" style="left:738px;width:117px;height:24px;top:1049px;background:#d8482a"></div>
  </section>

  <footer>
    <div class="abs footer-links">Privacy Policy &nbsp;|&nbsp;Terms of Use &nbsp;|&nbsp;Disclaimer</div>
    <div class="abs footer-copy">Copyright © 2014 DK Farrow</div>
  </footer>
</div>
</body>
</html>
```